Redesign of existing website for a corporate advisory business focussed on technology

We need a redesign of our website. We are a corporate advisory business based in Sydney. Our focus is on the technology and life-science sectors. We assist our clients with capital raisings, mergers and acquisitions and other corporate transactions.

Our business is called "Harbourline Capital Advisors"
Our current website is www.harbourlinecap.com.au

I'd like to see a complete re-design of the site. (I'm happy to keep any of the existing images - but equally happy to scrap them completely and "start again".)

My preference is that the logo remain as it is. However, I would be very open to a re-colouring of the logo if it works better with a new webiste design.

The content of the website will remain the same. I'd like one additional section - "News" - which will allow us to manually post news items and which will pull in news feeds from current and past clients.

In terms of positioning / look-and-feel:

Our clients fall into two categories. I'd like the website to appeal to both:

1. The first category is: Executives from established technology or life-science companies (private or public), who engage us to assist with strategy, capital raising, corporate transactions.

2. The second category is: Entrepreneurs looking for advice in accessing angel funding or venture capital. The site should appeal to young tech-savvy entrepreneurs who are looking to engage a firm to provide such assistance.

To accomodate both target groups, the overriding feel should be one of professionalism, stability, trust and expertise. However, while the site should look fairly "corporate", I'd like it to feel contemporary and have an element of creativity and flair, reflecting the fact that our clients are often early-stage, innovative, technology companies. (I know this might be a tricky balance...)

Target Market(s)

Potential clients. Typically executives at technology or life-science companies or (more typically) entrepreneurs building their own companies

Industry/Entity Type

Business

Requirements
Must have
• 1. All content on the existing website
2. An additional section called "News" that allows us to easily add news items or articles and ideally which accepts news feeds from a handful of past and present clients
3. An ability to easily update and edit content
Should not have
• The site should not have "gimmicks". (Definitely no devices like the moving arrow in the current site!)

It should be fairly conservative, while still feeling contemporary and fresh.

```html
<!DOCTYPE html>
<html lang="en">
<head>
<meta charset="utf-8">
<title>Harbourline Capital Advisors</title>
<link rel="stylesheet" href="https://fonts.googleapis.com/css2?family=Arimo:wght@400;700&display=swap">
<style>
:root{
  --orange:#f47a20;
  --ink:#111;
  --text:#333;
  --muted:#8a8a8a;
  --line:#d9d9d9;
  --page:#f3f3f3;
  --white:#fff;
}
*{margin:0;padding:0;box-sizing:border-box}
html,body{width:1200px;height:1018px;overflow:hidden}
body{position:relative;font-family:"Arimo",Arial,sans-serif;color:var(--text);
  background:linear-gradient(#d8d8d8 0,#f4f4f4 150px,#e6e6e6 151px,#fafafa 300px,#fafafa 430px,var(--page) 440px)}
a{color:inherit;text-decoration:none}
.abs{position:absolute}

/* header */
.brand{left:120px;top:17px;display:flex;align-items:center;gap:14px}
.brand-dot{width:69px;height:69px;border-radius:50%;background:var(--orange)}
.brand-name{font-size:25px;color:#444;white-space:nowrap}
.social{top:37px;display:flex;gap:6px}
.social span{display:block;width:31px;height:31px;border-radius:50%;background:var(--ink)}
.social span.accent{background:var(--orange)}
.search{left:884px;top:36px;width:191px;height:33px;display:flex}
.search-field{flex:1;background:var(--white);border:1px solid #ccc;font-size:12px;color:#888;padding:9px 14px}
.search-btn{width:29px;background:#666;display:flex;align-items:center;justify-content:center}

/* nav */
.nav{left:120px;top:103px;width:737px;height:46px;background:var(--ink);display:flex}
.nav a{color:var(--white);font-size:14px;line-height:46px;text-align:center;white-space:nowrap;flex:none}
.nav a.home{width:103px}
.nav a.services{width:134px}
.nav a.team{width:111px}
.nav a.experience{width:170px}
.nav a.contact{width:99px}
.nav a.news{width:86px}
.nav a.active{background:var(--orange)}
.phone{left:857px;top:103px;width:223px;height:48px;background:var(--orange);color:var(--white);
  font-size:19px;display:flex;align-items:center;justify-content:center;gap:10px;white-space:nowrap}
.call-note{left:1112px;top:153px;width:58px;height:26px;background:#e2e2e2;border-radius:3px}

/* hero */
.hero{left:120px;top:149px;width:960px;height:382px;overflow:hidden;
  background:linear-gradient(90deg,#c9c9c9 0,#a9aaab 40%,#8e9296 60%,#7a7f86 100%)}
.hero-photo{position:absolute;right:0;top:0;width:340px;height:382px;
  background:linear-gradient(160deg,#c8ccd1,#6f747b 60%,#3c4048)}
.hero-panel{position:absolute;left:0;top:57px;width:605px;height:202px;background:rgba(60,60,60,.78);color:var(--white);padding:36px 0 0 51px}
.hero-kicker{font-size:26px;font-weight:700}
.hero-title{font-size:32px;font-weight:700;margin-top:6px;white-space:nowrap}
.hero-title .amp{color:var(--orange)}
.hero-points{list-style:none;margin-top:10px;font-size:13px}
.hero-points li{display:flex;align-items:center;gap:9px;margin-bottom:7px}
.tick{width:12px;height:12px;border-radius:50%;background:var(--white);display:inline-flex;align-items:center;justify-content:center}
.hero-cta{position:absolute;left:48px;top:279px;width:250px;height:50px;background:var(--ink);color:var(--white);
  font-size:23px;font-weight:700;display:flex;align-items:center;justify-content:center;border-radius:2px}

/* columns */
.cols{left:120px;top:531px;width:960px;height:297px;display:flex;border-bottom:1px solid var(--line)}
.col{height:100%;background:linear-gradient(#f0f0f0,#e4e4e4)}
.col.news{width:321px}
.col.about{width:318px;background:var(--white)}
.col.touch{width:321px}
.col-head{height:57px;background:linear-gradient(#e9e9e9,#d5d5d5);display:flex;align-items:center;gap:12px;padding-left:32px;
  font-size:22px;font-weight:400;color:#555}
.col.about .col-head{background:linear-gradient(#f6f6f6,#e6e6e6)}
.news-item{padding:0 0 0 28px;margin-top:31px}
.news-item + .news-item{margin-top:20px}
.news-title{font-size:15px;font-weight:400;color:#111;display:flex;gap:8px;align-items:center}
.news-title::before{content:"";width:4px;height:4px;background:var(--orange)}
.news-body{font-size:12px;line-height:20px;color:#555;margin-top:6px;padding-left:3px;width:280px}
.more{color:var(--orange);text-decoration:underline}
.about-photo{margin:15px 0 0 27px;width:264px;height:134px;background:linear-gradient(135deg,#dde6ee,#8fa3b4 55%,#3f4a58)}
.about-text{font-size:12px;line-height:16px;color:#666;margin:20px 0 0 27px;width:265px}
.touch-lead{font-size:12px;line-height:16px;color:#888;margin:34px 0 0 27px;width:270px}
.contact-list{list-style:none;margin:18px 0 0 27px;font-size:12px;color:#666}
.contact-list li{display:flex;gap:12px;margin-bottom:10px;line-height:16px}
.contact-list svg{flex:none;margin-top:1px}

/* footer */
.footer{left:120px;top:845px;width:960px;height:146px;background:var(--white);border:1px solid #ccc;border-radius:5px}
.foot-links{position:absolute;top:29px;list-style:none;font-size:12px;line-height:19px;color:#222}
.foot-links .on{color:var(--orange)}
.foot-copy{position:absolute;left:207px;top:96px;font-size:12px;line-height:15px;color:#444}
.divider{position:absolute;top:14px;width:1px;height:118px;background:var(--line)}
.foot-social{position:absolute;left:483px;top:31px;display:flex;gap:9px}
.foot-social span{width:31px;height:31px;border-radius:50%;background:var(--ink)}
.foot-social span.accent{background:var(--orange)}
.foot-social-rule{position:absolute;left:483px;top:80px;width:152px;height:1px;background:var(--line)}
.powered{position:absolute;left:485px;top:94px;font-size:12px;color:#999;white-space:nowrap}
.foot-brand{position:absolute;left:708px;top:26px;display:flex;align-items:center;gap:10px}
.foot-brand .brand-dot{width:38px;height:38px}
.foot-brand .brand-name{font-size:14px}
</style>
</head>
<body>

<header>
  <div class="abs brand">
    <span class="brand-dot"></span>
    <span class="brand-name">Harbourline Capital Advisors</span>
  </div>
  <div class="abs social" style="left:725px">
    <span class="accent"></span><span></span><span></span><span></span>
  </div>
  <div class="abs search">
    <div class="search-field">Search</div>
    <div class="search-btn">
      <svg width="13" height="13" viewBox="0 0 13 13"><circle cx="5.5" cy="5.5" r="4" fill="none" stroke="#fff" stroke-width="1.8"/><line x1="8.5" y1="8.5" x2="12" y2="12" stroke="#fff" stroke-width="2"/></svg>
    </div>
  </div>
</header>

<nav class="abs nav">
  <a href="#" class="home">HOME</a>
  <a href="#" class="services active">OUR SERVICES</a>
  <a href="#" class="team">OUR TEAM</a>
  <a href="#" class="experience">OUR EXPERIENCE</a>
  <a href="#" class="contact">CONTACT</a>
  <a href="#" class="news">NEWS</a>
</nav>
<div class="abs phone">
  <svg width="22" height="16" viewBox="0 0 22 16"><path d="M1 5c5-5 15-5 20 0l-3 3-3-2v-2c-3-1-5-1-8 0v2l-3 2z M5 10h12v5H5z" fill="#fff"/></svg>
  +1 (110) 555-0148
</div>
<div class="abs call-note" role="img" aria-label="Handwritten Call Us note with a small arrow"></div>

<section class="abs hero">
  <div class="hero-photo" role="img" aria-label="Photo of a smiling businessman in a suit talking on a mobile phone"></div>
  <div class="hero-panel">
    <p class="hero-kicker">Our Focus is on the</p>
    <h1 class="hero-title">Technology <span class="amp">&amp;</span> Life-Science Sectors</h1>
    <ul class="hero-points">
      <li><span class="tick"><svg width="8" height="8" viewBox="0 0 8 8"><path d="M1 4l2 2 4-4" fill="none" stroke="#444" stroke-width="1.5"/></svg></span>Executives from established technology or life-science companies.</li>
      <li><span class="tick"><svg width="8" height="8" viewBox="0 0 8 8"><path d="M1 4l2 2 4-4" fill="none" stroke="#444" stroke-width="1.5"/></svg></span>Entrepreneurs looking for advice in accessing angel funding or venture capital.</li>
    </ul>
  </div>
  <a href="#" class="hero-cta">Get Our Services</a>
</section>

<section class="abs cols">
  <div class="col news">
    <h2 class="col-head">
      <svg width="22" height="20" viewBox="0 0 22 20"><rect x="1" y="3" width="20" height="16" rx="2" fill="none" stroke="#333" stroke-width="2"/><rect x="1" y="3" width="20" height="5" fill="#333"/><rect x="5" y="0" width="2" height="5" fill="#333"/><rect x="15" y="0" width="2" height="5" fill="#333"/></svg>
      Latest News
    </h2>
    <article class="news-item">
      <h3 class="news-title">Why I left San Francisco</h3>
      <p class="news-body">Winch 5, my global tour of innovation, is actually the natural continuation of the 16 years I spent in Mexico, and the 14 years in... <a class="more" href="#">READ MORE</a></p>
    </article>
    <article class="news-item">
      <h3 class="news-title">Why I left San Francisco</h3>
      <p class="news-body">Winch 5, my global tour of innovation, is actually the natural continuation of the 16 years I spent in Mexico, and the 14 years in... <a class="more" href="#">READ MORE</a></p>
    </article>
  </div>
  <div class="col about">
    <h2 class="col-head">
      <svg width="22" height="22" viewBox="0 0 22 22"><rect x="1" y="4" width="16" height="16" rx="2" fill="none" stroke="#333" stroke-width="2"/><path d="M8 14l1-4 9-9 3 3-9 9z" fill="#333"/></svg>
      About Us
    </h2>
    <div class="about-photo" role="img" aria-label="Photo of a business team meeting around a table"></div>
    <p class="about-text">Lorem ipsum dolor sit amet, conse ctetur adipisicing sed do eiusmod tempor incididunt ut labore et dolore - <a class="more" href="#">READ MORE</a></p>
  </div>
  <div class="col touch">
    <h2 class="col-head">
      <svg width="24" height="17" viewBox="0 0 24 17"><rect x="0" y="0" width="24" height="17" rx="1" fill="#333"/><path d="M1 1l11 9 11-9" fill="none" stroke="#e9e9e9" stroke-width="1.5"/></svg>
      Get In Touch
    </h2>
    <p class="touch-lead">Lorem ipsum dolor sit amet, conse ctetur elit, sed do eiusmod tempor adipisicing</p>
    <ul class="contact-list">
      <li><svg width="12" height="16" viewBox="0 0 12 16"><path d="M6 0a6 6 0 0 1 6 6c0 4-6 10-6 10S0 10 0 6a6 6 0 0 1 6-6z" fill="#888"/><circle cx="6" cy="6" r="2" fill="#eee"/></svg><span>12-C, Marlow Lane, Opposite City Clinic,<br>New York, USA - 219</span></li>
      <li><svg width="12" height="16" viewBox="0 0 12 16"><rect x="1" y="0" width="10" height="16" rx="2" fill="#888"/><rect x="3" y="2" width="6" height="9" fill="#eee"/></svg><span>+91 90000 41872</span></li>
      <li><svg width="13" height="10" viewBox="0 0 13 10"><rect x=".5" y=".5" width="12" height="9" fill="none" stroke="#888"/><path d="M.5 .5l6 5 6-5" fill="none" stroke="#888"/></svg><span>info@harbourlinecap.com.au</span></li>
    </ul>
  </div>
</section>

<footer class="abs footer">
  <ul class="foot-links" style="left:38px">
    <li>Benefits</li>
    <li class="on">Our Services</li>
    <li>Our Team</li>
    <li>Our Experience</li>
    <li>Contact Us</li>
  </ul>
  <span class="divider" style="left:168px"></span>
  <ul class="foot-links" style="left:207px">
    <li>Privacy Policy</li>
    <li class="on">Terms of Use</li>
    <li>Disclaimer</li>
  </ul>
  <p class="foot-copy">All Right Reserved Copyright © 2012<br>www.harbourlinecap.com.au</p>
  <span class="divider" style="left:447px"></span>
  <div class="foot-social"><span></span><span></span><span class="accent"></span><span></span></div>
  <span class="foot-social-rule"></span>
  <p class="powered">Powered By : Northgate Studio</p>
  <span class="divider" style="left:672px"></span>
  <div class="foot-brand">
    <span class="brand-dot"></span>
    <span class="brand-name">Harbourline Capital Advisors</span>
  </div>
</footer>

</body>
</html>
```